Florida-based Coastal Landscaping Company Needs Letterhead Designs

We are a newly established Florida-based, coastal landscaping company that is looking for some really innovative flyers that we can use to get our name our to affluent consumers that live on the coast of Florida (think on the beach) and small to medium sized businesses in the same area. We will be handing out 100s of thousands of these, so need a great design

Target Market(s)

Affluent consumers and small to medium sized businesses

Industry/Entity Type

It Company

Font styles to use
Sans Serif

Colors

Designer to choose colors to be used in the design.

Requirements
Must have
• Need to have company name, logo, individual name, phone number and contact info
Nice to have
• Florida - looking, island looking / paradise, but needs to focus on the landscaping elements
Should not have
• Regular generic lawn company letterhead designs. We are a top tier landscape design / build plus maintenance firm, so not your mom and pop lawn mowing company

```html
<!DOCTYPE html>
<html lang="en">
<head>
<meta charset="utf-8">
<title>Shoreline Grove Letterhead</title>
<link rel="stylesheet" href="https://fonts.googleapis.com/css2?family=Open+Sans:wght@400;600&display=swap">
<style>
  :root {
    --backdrop: #c4ebf5;
    --paper: #ffffff;
    --brand-blue: #2cb3dc;
    --brand-blue-soft: rgba(44, 179, 220, 0.10);
    --ink: #1d1d1d;
    --muted: #6b6b6b;
    --tile: #ececec;
    --tile-dark: #e1e1e1;
    --footer-band: #f3f3f3;
  }
  * { box-sizing: border-box; margin: 0; padding: 0; }
  html, body {
    width: 1200px; height: 784px; overflow: hidden;
    background: var(--backdrop);
    font-family: "Open Sans", Arial, sans-serif;
  }
  .stage {
    width: 1200px; height: 784px;
    display: flex; align-items: center; justify-content: center;
  }
  .letterhead {
    position: relative;
    width: 556px; height: 720px;
    background: var(--paper);
    box-shadow: 0 6px 18px rgba(40, 120, 150, 0.18);
    overflow: hidden;
  }
  .letterhead__art {
    position: absolute; inset: 0;
    width: 100%; height: 100%;
  }
  .wave-area {
    position: absolute;
    left: 0; top: 240px;
    width: 556px; height: 380px;
    background: linear-gradient(160deg, rgba(255,255,255,0) 20%, var(--brand-blue-soft) 50%, rgba(255,255,255,0) 80%);
  }
  .brand {
    position: absolute; top: 34px; left: 40px;
    display: flex; align-items: center; gap: 8px;
  }
  .brand__mark {
    width: 10px; height: 10px; border-radius: 50%;
    background: var(--brand-blue);
  }
  .brand__name {
    font-weight: 600; font-size: 17px; letter-spacing: 2px;
    color: var(--ink);
  }
  .contact {
    position: absolute; left: 0; right: 0; bottom: 22px;
    padding: 0 28px;
    display: flex; justify-content: space-between; align-items: center;
    font-size: 7.2px; color: var(--muted);
  }
  .contact__item { display: flex; align-items: center; gap: 3px; white-space: nowrap; }
  .contact__icon { width: 8px; height: 8px; flex: none; }
</style>
</head>
<body>
<main class="stage">
  <article class="letterhead">
    <svg class="letterhead__art" viewBox="0 0 556 720" aria-hidden="true">
      <polygon points="0,0 150,0 0,14" fill="var(--brand-blue)" opacity="0.85"/>
      <polygon points="556,640 556,720 420,720" fill="#d9d9d9" opacity="0.7"/>
      <rect x="0" y="684" width="556" height="36" fill="var(--footer-band)"/>
      <g fill="var(--tile)">
        <rect x="440" y="210" width="42" height="42"/>
        <rect x="488" y="210" width="36" height="30"/>
        <rect x="490" y="248" width="56" height="48" fill="var(--tile-dark)"/>
        <rect x="430" y="262" width="52" height="56"/>
        <rect x="530" y="200" width="26" height="24"/>
      </g>
      <g fill="var(--tile)">
        <rect x="0" y="560" width="40" height="40"/>
        <rect x="46" y="540" width="70" height="60"/>
        <rect x="10" y="608" width="58" height="50" fill="var(--tile-dark)"/>
        <rect x="76" y="608" width="44" height="40" fill="var(--tile-dark)"/>
        <rect x="0" y="664" width="36" height="20"/>
      </g>
    </svg>

    <div class="wave-area" role="img" aria-label="Soft blue decorative wave sweeping down the page"></div>

    <header class="brand">
      <span class="brand__mark"></span>
      <span class="brand__name">SHORELINE GROVE</span>
    </header>

    <footer class="contact">
      <span class="contact__item">
        <svg class="contact__icon" viewBox="0 0 10 10"><circle cx="5" cy="5" r="5" fill="var(--brand-blue)"/><path d="M5 2a2 2 0 0 0-2 2c0 1.5 2 4 2 4s2-2.5 2-4a2 2 0 0 0-2-2z" fill="#fff"/></svg>
        P.O. Box 4810 Seabright, FL 33902
      </span>
      <span class="contact__item">
        <svg class="contact__icon" viewBox="0 0 10 10"><circle cx="5" cy="5" r="5" fill="var(--brand-blue)"/><path d="M3 2.5h1.3l.5 1.4-.8.6a4 4 0 0 0 1.5 1.5l.6-.8 1.4.5V7a.6.6 0 0 1-.6.6A4.4 4.4 0 0 1 2.4 3.1.6.6 0 0 1 3 2.5z" fill="#fff"/></svg>
        (000) 555-0142
      </span>
      <span class="contact__item">
        <svg class="contact__icon" viewBox="0 0 10 10"><circle cx="5" cy="5" r="5" fill="var(--brand-blue)"/><rect x="2.6" y="3" width="4.8" height="4" fill="#fff"/><rect x="3.4" y="2" width="3.2" height="1.4" fill="#fff"/></svg>
        (000) 555-0178
      </span>
      <span class="contact__item">
        <svg class="contact__icon" viewBox="0 0 10 10"><circle cx="5" cy="5" r="5" fill="var(--brand-blue)"/><rect x="2.3" y="3" width="5.4" height="4" fill="#fff"/><path d="M2.3 3 5 5.2 7.7 3" fill="none" stroke="var(--brand-blue)" stroke-width=".6"/></svg>
        hello@shorelinegrovefl.com
      </span>
      <span class="contact__item">
        <svg class="contact__icon" viewBox="0 0 10 10"><circle cx="5" cy="5" r="5" fill="var(--brand-blue)"/><circle cx="5" cy="5" r="2.6" fill="none" stroke="#fff" stroke-width=".7"/><path d="M2.4 5h5.2M5 2.4c-1.2 1.4-1.2 3.8 0 5.2M5 2.4c1.2 1.4 1.2 3.8 0 5.2" fill="none" stroke="#fff" stroke-width=".5"/></svg>
        www.shorelinegrovefl.com
      </span>
    </footer>
  </article>
</main>
</body>
</html>
```